Harald turning 50 invitation

Celebrating my 50th years birthday party in the summer vacation village fjällbacka at the westcoast sweden. Se We have our summer house in that area. The party will be at main hotel where people will also stay. Theme of the evening is South American food, meat, caprinhia etc. not costume party though. Want a good looking and stylish invitation to send out a pdf. And possible printed. West coast Sweden is very much about blue sea and red and white houses I need to be able to update text myself.

Target Market(s)

My friends

Colors
33a6d7
0692cd
abd037
ffffff

Requirements
Must have
• Pictures of the small town Havsklint
Nice to have
• Just a Anselmo always and inviting feeling for a great party

```html
<!DOCTYPE html>
<html lang="en">
<head>
<meta charset="utf-8">
<title>Harald's 50th Birthday Invitation</title>
<link rel="stylesheet" href="https://fonts.googleapis.com/css2?family=Roboto+Condensed:ital,wght@0,700;1,400&family=Roboto:ital,wght@0,400;1,400&family=Orbitron:wght@500&family=Archivo+Black&display=swap">
<style>
  :root {
    --sea-blue: #33a6d7;
    --deep-blue: #0692cd;
    --lime: #abd037;
    --neon-lime: #c6f23a;
    --white: #ffffff;
    --night: #12171d;
    --page: #f2f2f2;
  }
  * { margin: 0; padding: 0; box-sizing: border-box; }
  html, body {
    width: 1200px; height: 1000px; overflow: hidden;
    background: var(--page);
  }
  .invitation {
    position: absolute; left: 307px; top: 18px;
    width: 668px; height: 947px;
    background: var(--night);
    overflow: hidden;
    color: var(--white);
    font-family: "Roboto", Arial, sans-serif;
  }
  .town-photo {
    position: absolute; left: 0; top: 290px; width: 668px; height: 657px;
    background:
      linear-gradient(180deg, var(--night) 0%, rgba(18,23,29,0.55) 18%, rgba(30,26,26,0.55) 60%, rgba(20,24,30,0.8) 100%),
      linear-gradient(180deg, #3a2a26 0%, #4a302a 35%, #2c3138 65%, #1f2a36 100%);
  }
  .host-photo {
    position: absolute; left: 40px; top: 142px; width: 118px; height: 176px;
    background: linear-gradient(180deg, #7b6a5c 0%, #2a3b55 40%, #1f2d44 100%);
    border-radius: 46px 46px 4px 4px;
  }
  .rule { position: absolute; background: var(--white); }
  .rule--right { left: 625px; top: 0; width: 8px; height: 470px; }
  .rule--left { left: 133px; top: 430px; width: 6px; height: 517px; }

  .headline {
    position: absolute; right: 367px; top: 246px;
    font-family: "Roboto Condensed", "Arial Narrow", sans-serif;
    font-weight: 700; font-size: 30px; line-height: 29px;
    text-align: right; letter-spacing: 0.2px;
  }
  .neon { position: absolute; overflow: visible; }
  .neon--name { left: 48px; top: 296px; }
  .neon--age { left: 312px; top: 180px; }
  .birthday { position: absolute; left: 52px; top: 392px; }

  .details {
    position: absolute; right: 46px; text-align: right;
  }
  .details__date {
    top: 582px;
    font-family: "Roboto Condensed", "Arial Narrow", sans-serif;
    font-weight: 700; font-size: 29.5px; line-height: 35px;
  }
  .details__venue { top: 657px; font-size: 21.5px; line-height: 26px; }
  .details__menu { top: 708px; font-style: italic; font-size: 22px; line-height: 27px; }
  .details__rsvp { top: 848px; font-size: 20.5px; line-height: 26px; }
</style>
</head>
<body>
<main class="invitation">
  <div class="town-photo" role="img" aria-label="Evening photo of a seaside village harbour with red and white houses and moored boats"></div>
  <div class="rule rule--right"></div>
  <div class="rule rule--left"></div>

  <div class="host-photo" role="img" aria-label="Photo of Harald raising a glass of champagne"></div>

  <p class="headline">JOIN US TO<br>CELEBRATE</p>

  <svg class="neon neon--name" width="270" height="80" viewBox="0 0 270 80" aria-label="Harald's">
    <defs>
      <filter id="blue-glow" x="-20%" y="-40%" width="140%" height="180%">
        <feGaussianBlur stdDeviation="4" result="b"/>
        <feMerge><feMergeNode in="b"/><feMergeNode in="SourceGraphic"/></feMerge>
      </filter>
    </defs>
    <text x="0" y="72" textLength="256" lengthAdjust="spacingAndGlyphs"
          font-family="'Archivo Black', Arial, sans-serif" font-size="64"
          fill="rgba(51,166,215,0.15)" stroke="#33a6d7" stroke-width="3" filter="url(#blue-glow)">HARALD’S</text>
  </svg>

  <svg class="neon neon--age" width="310" height="200" viewBox="0 0 310 200" aria-label="50th">
    <defs>
      <filter id="lime-glow" x="-20%" y="-20%" width="140%" height="140%">
        <feGaussianBlur stdDeviation="5" result="b"/>
        <feMerge><feMergeNode in="b"/><feMergeNode in="SourceGraphic"/></feMerge>
      </filter>
    </defs>
    <g font-family="'Archivo Black', Arial, sans-serif" filter="url(#lime-glow)">
      <text x="6" y="186" font-size="214" textLength="252" lengthAdjust="spacingAndGlyphs"
            fill="none" stroke="#c6f23a" stroke-width="3">50</text>
      <text x="6" y="186" font-size="214" textLength="252" lengthAdjust="spacingAndGlyphs"
            fill="none" stroke="#abd037" stroke-width="16" stroke-opacity="0.25">50</text>
      <text x="268" y="76" font-size="20" fill="none" stroke="#c6f23a" stroke-width="1.5">TH</text>
    </g>
  </svg>

  <svg class="birthday" width="570" height="140" viewBox="0 0 570 140" aria-label="Birthday">
    <text x="0" y="122" textLength="558" lengthAdjust="spacingAndGlyphs"
          font-family="'Orbitron', Arial, sans-serif" font-weight="500" font-size="134"
          fill="#ffffff">BIRTHDAY</text>
  </svg>

  <p class="details details__date">WEDNESDAY I OCTOBER 23 2019<br>AT SIX O’CLOCK IN THE EVENING</p>
  <p class="details details__venue">at Hotel Name, Hotel address, Havsklint</p>
  <p class="details details__menu">South American food, meat and<br>Caipirinha will be served.</p>
  <p class="details details__rsvp">RSVP to Harald by<br>October 23, 2019 at 0701 55 20 30</p>
</main>
</body>
</html>
```